Classic and neutral book cover design

We are looking for a classic and neutral book cover design to be used as the template for a series of books to be published. We are hence looking for a template that will allow us to easily change the title name for all books in this series.
The use of very few colours (black and white is welcome) and few design elements is a big bonus. As a source of inspiration we would like to ask you to view the very simple and
If you think you have a cool idea that can add a twist to the formal classic look don't hesitate. Go for it !
Work will be done for a 30 year old Sweden based cultural non-profit called VĂ©lra (www.velrafoundation.example). We work with the publishing and supporting of post-modern art and literature addressing contemporary topics but are also involved in assisting projects of cultural preservation.
Target Market(s)
The audience is expected to have some form of interest in culture but could range from hobbyist readers to tenure track scholars
Industry/Entity Type
Non-Profit
Requirements
Must have
- General:
- Classic and neutral feel
- Preferably very simple and few shapes
- usage of few colours (black and white is welcome)
Information to be displayed on the cover is:
- Author
- Title
- type of work e.g. play/novel (optional)
- publishing house (in this case "Velra Publishing")
Nice to have
- ideas to prevent it from become boring are of course welcome
Should not have
- - too many colours

```html
<!DOCTYPE html>
<html lang="fr">
<head>
<meta charset="utf-8">
<title>Le Passant — Vélra Publishing series cover</title>
<link rel="stylesheet" href="https://fonts.googleapis.com/css2?family=Bodoni+Moda:opsz,wght@6..96,500;6..96,600&display=swap">
<style>
  :root {
    --stage: #f4f4f4;
    --paper: #ffffff;
    --ink: #1b1b1b;
    --cover-dark: #3a3a3c;
    --band-grey: #d9d9d9;
    --accent-blue: #9ec8ea;
    --footer-grey: #ececec;
    --author-ink: #e6e6e6;
  }
  * { margin: 0; padding: 0; box-sizing: border-box; }
  html, body {
    width: 1200px;
    height: 1000px;
    overflow: hidden;
    background: var(--stage);
  }
  .canvas {
    position: relative;
    width: 1200px;
    height: 1000px;
  }
  .cover {
    position: absolute;
    left: 320px;
    top: 80px;
    width: 560px;
    height: 840px;
    background: var(--paper);
    box-shadow: 0 2px 10px rgba(0,0,0,0.12);
    overflow: hidden;
  }
  .title-panel {
    position: absolute;
    left: 0; top: 0;
    width: 100%;
    height: 195px;
    background: var(--paper);
    display: flex;
    align-items: center;
    justify-content: center;
    padding-top: 30px;
  }
  .book-title {
    font-family: "Bodoni Moda", "Didot", serif;
    font-weight: 600;
    font-size: 50px;
    color: var(--ink);
    letter-spacing: 0.5px;
  }
  .texture-band {
    position: absolute;
    left: 0; top: 195px;
    width: 100%;
    height: 30px;
    background: linear-gradient(180deg, #e2e2e2, var(--band-grey));
  }
  .accent-rule {
    position: absolute;
    left: 0; top: 225px;
    width: 100%;
    height: 8px;
    background: var(--accent-blue);
  }
  .body-panel {
    position: absolute;
    left: 0; top: 233px;
    width: 100%;
    height: 472px;
    background: var(--cover-dark);
  }
  .author {
    position: absolute;
    top: 28px;
    width: 100%;
    text-align: center;
    font-family: "Bodoni Moda", "Didot", serif;
    font-weight: 500;
    font-variant: small-caps;
    font-size: 24px;
    letter-spacing: 1px;
    color: var(--author-ink);
  }
  .footer-panel {
    position: absolute;
    left: 0; top: 705px;
    width: 100%;
    height: 135px;
    background: var(--footer-grey);
  }
  .publisher-tab {
    position: absolute;
    left: 190px;
    top: 658px;
    width: 180px;
    height: 47px;
    background: var(--footer-grey);
    display: flex;
    align-items: center;
    justify-content: center;
  }
  .publisher-name {
    font-family: "Bodoni Moda", "Didot", serif;
    font-weight: 600;
    font-size: 24px;
    letter-spacing: 1px;
    color: var(--ink);
    padding-top: 4px;
  }
</style>
</head>
<body>
  <main class="canvas">
    <article class="cover">
      <header class="title-panel">
        <h1 class="book-title">Le Passant</h1>
      </header>
      <div class="texture-band" role="img" aria-label="Fine speckled grey decorative pattern band"></div>
      <div class="accent-rule"></div>
      <section class="body-panel">
        <p class="author">Armand Castel</p>
      </section>
      <footer class="footer-panel"></footer>
      <div class="publisher-tab">
        <span class="publisher-name">VÉLRA</span>
      </div>
    </article>
  </main>
</body>
</html>
```